Web Design Project

This is a wordpress project for a newly formed biologics company based in the US with international clientele. We do manufacturing of biologically based raw materials using a state of the art facility....Our logo must be incorporated....logo colors Navy and Gray. It is fine to use some color in web design. The viewer will primarily be industry folk.

Velorast Biologics, LLC is a contract manufacturing organization which produces biologically-based raw materials derived primarily from human plasma. The company services include extraction and purification of plasma components, especially proteins and enzymes. The business focuses on biotherapeutics, diagnostic and veterinary markets worldwide.

5 pages a bad example of first page can be found in attached files.....
use stock photos of labs and clean rooms.
Updates

Project Deadline Extended
Reason: I need a bit more time tonprovide feedback.

Project Deadline Extended
Reason: needed time to evaluate existing options

Target Market(s)

target market Pharmaceutical companies and research universities

Industry/Entity Type

Veterinary

Requirements
Must have
• our logo...we will provide some graphics...

```html
<!DOCTYPE html>
<html lang="en">
<head>
<meta charset="utf-8">
<title>Velorast Biologics – Facilities</title>
<link rel="stylesheet" href="https://fonts.googleapis.com/css2?family=PT+Sans:wght@400;700&family=PT+Sans+Narrow:wght@400;700&display=swap">
<style>
:root{
  --navy:#0b2a55;
  --navy-deep:#061a36;
  --blue:#1565b8;
  --blue-bright:#2f86d6;
  --cyan-line:#7fd8e6;
  --gray-light:#eeeeef;
  --gray-mid:#c9c9cc;
  --gray-bar:#a9a9ad;
  --text-navy:#13305c;
  --footer-link:#9fb4cc;
  --footer-muted:#6f87a6;
  --white:#ffffff;
}
*{box-sizing:border-box;margin:0;padding:0}
html,body{width:1168px;height:1200px;overflow:hidden}
body{position:relative;background:var(--gray-light);font-family:"PT Sans",Arial,sans-serif}
.abs{position:absolute}

.site-header{left:0;top:0;width:1168px;height:86px;background:linear-gradient(#ffffff,#d8d8da);border-bottom:2px solid var(--cyan-line)}
.brand{left:54px;top:18px;display:flex;align-items:center;gap:10px}
.brand-mark{width:46px;height:46px;border-radius:50%;background:var(--navy)}
.brand-name{font-size:24px;font-weight:700;color:var(--navy)}
.main-nav{right:46px;top:30px;display:flex;gap:14px;align-items:center}
.main-nav a{font-size:24px;color:var(--white);text-decoration:none;padding:4px 10px;text-shadow:0 1px 2px rgba(0,0,0,.55)}
.main-nav a.is-current{border:1px solid var(--blue);border-radius:8px;background:linear-gradient(#e8eef6,#b9c8da)}

.hero{left:30px;top:88px;width:1098px;height:246px;background:radial-gradient(ellipse at 50% 30%,#2e78c6,var(--navy) 75%);overflow:hidden}
.hero-band{left:0;bottom:0;width:100%;height:40px;background:linear-gradient(#1b74c7,#0a3c78)}
.slide{border:5px solid rgba(235,242,250,.8)}
.slide-side{top:32px;width:155px;height:192px;background:linear-gradient(#dfe7ee,#b9c7d3)}
.slide-main{left:395px;top:10px;width:333px;height:226px;background:linear-gradient(#f2f4f6,#c5cdd4);border-color:#e9eef3}
.pager{left:510px;top:214px;display:flex;gap:9px}
.pager span{width:22px;height:22px;border-radius:50%;background:var(--blue-bright);color:var(--white);font-size:14px;text-align:center;line-height:22px}
.pager span.is-active{background:#0a1e3c}

.section-bar{left:46px;top:354px;width:1050px;height:50px;background:var(--gray-bar);border-bottom:2px solid var(--cyan-line)}
.section-title{left:24px;top:5px;font-family:"PT Sans Narrow",Arial,sans-serif;font-weight:700;font-size:32px;color:var(--white);text-shadow:0 1px 2px rgba(0,0,0,.4)}
.search-box{right:14px;top:8px;width:208px;height:30px;background:var(--white);border:1px solid #999;border-radius:3px;font-size:12px;color:#777;padding:7px 10px}
.search-btn{right:0;top:0;width:26px;height:28px;background:#ddd;border-left:1px solid #aaa}

.content{left:0;top:404px;width:1168px;height:522px;background:linear-gradient(#e9e9eb 0%,#dcdcde 70%,#9d9da1 100%)}
.thumb{border:2px solid #3a5f8e}
.feature-text{left:317px;width:680px;font-family:"PT Sans Narrow",Arial,sans-serif;font-size:20px;line-height:30px;color:var(--text-navy)}
.divider{left:315px;width:667px;border-top:2px dashed #a5a5aa}
.more{left:990px;font-size:18px;color:#888;letter-spacing:2px}

.site-footer{left:0;top:926px;width:1168px;height:274px;background:linear-gradient(var(--navy),var(--navy-deep))}
.footer-col{top:54px;font-size:20px;line-height:26.5px}
.footer-col a{display:block;color:var(--footer-muted);text-decoration:none}
.footer-col.primary a{color:var(--footer-link)}
.col-rule{top:30px;width:1px;height:176px;background:#1c3d68}
.follow{left:956px;top:48px;font-size:20px;color:var(--footer-muted)}
.social{top:82px;width:28px;height:28px;background:#4f8fd0;border-radius:4px}
.footer-search{left:958px;top:140px;width:158px;height:28px;background:var(--navy);border:1px solid #3a6aa3;color:var(--white);font-size:14px;font-weight:700;padding:4px 10px}
.footer-search i{position:absolute;right:0;top:0;width:18px;height:26px;background:#7f93aa}
.copyright{left:0;top:232px;width:1168px;text-align:center;font-size:13px;color:#2a5486}
</style>
</head>
<body>

<header class="site-header abs">
  <div class="brand abs"><span class="brand-mark"></span><span class="brand-name">Velorast Biologics</span></div>
  <nav class="main-nav abs">
    <a href="#">Home</a><a href="#" class="is-current">Facilities</a><a href="#">Team</a><a href="#">Announcements</a><a href="#">Contact</a>
  </nav>
</header>

<section class="hero abs">
  <div class="hero-band abs"></div>
  <div class="slide slide-side abs" style="left:240px" role="img" aria-label="Clean room corridor photo"></div>
  <div class="slide slide-side abs" style="left:728px;width:219px" role="img" aria-label="Bright clean room interior photo"></div>
  <div class="slide slide-main abs" role="img" aria-label="Laboratory with white benches photo"></div>
  <div class="pager abs"><span>1</span><span>2</span><span class="is-active">3</span><span>4</span></div>
</section>

<main>
  <div class="content abs"></div>
  <div class="section-bar abs">
    <h1 class="section-title abs">Facilities</h1>
    <div class="search-box abs">Search<span class="search-btn abs"></span></div>
  </div>

  <div class="thumb abs" style="left:70px;top:433px;width:205px;height:130px;background:linear-gradient(#e6ebf0,#9ea9b3)" role="img" aria-label="Laboratory bench with equipment"></div>
  <p class="feature-text abs" style="top:464px">VBL is currently in process of commissioning and validating a 3000 sq/ft cGMP clean-rooms.</p>
  <div class="divider abs" style="top:571px"></div><span class="more abs" style="top:557px">&gt;&gt;</span>

  <div class="thumb abs" style="left:69px;top:581px;width:209px;height:139px;background:linear-gradient(#edf1f4,#a8b0b8)" role="img" aria-label="Long clean room corridor"></div>
  <p class="feature-text abs" style="top:610px">The facility has a capacity of producing up to 35,000 liters of plasma, and additional capacity to expand up to 100,000 liters</p>
  <div class="divider abs" style="top:726px"></div><span class="more abs" style="top:712px">&gt;&gt;</span>

  <div class="thumb abs" style="left:67px;top:737px;width:215px;height:143px;background:linear-gradient(#dfe6ec,#8fa4b6)" role="img" aria-label="Technician in protective suit working in a clean room"></div>
  <p class="feature-text abs" style="top:755px">State-of-the-art facilities based on the Corvanta Single Use Disposable plastic bags. Which reduces risks of cross-contamination between batches and represents a substantial savings in operation and staffing for our customers.</p>
</main>

<footer class="site-footer abs">
  <nav class="footer-col primary abs" style="left:74px"><a href="#">Home</a><a href="#">Facilities</a><a href="#">Team</a><a href="#">Links</a><a href="#">Contact</a></nav>
  <div class="col-rule abs" style="left:215px"></div>
  <nav class="footer-col abs" style="left:260px"><a href="#">Some Quick Links</a><a href="#">Some Quick Links</a><a href="#">Some Quick Links</a><a href="#">Some Quick Links</a><a href="#">Some Quick Links</a></nav>
  <div class="col-rule abs" style="left:464px"></div>
  <nav class="footer-col abs" style="left:490px"><a href="#">Some Quick Links</a><a href="#">Some Quick Links</a><a href="#">Some Quick Links</a><a href="#">Some Quick Links</a><a href="#">Some Quick Links</a></nav>
  <div class="col-rule abs" style="left:695px"></div>
  <nav class="footer-col abs" style="left:728px"><a href="#">Some Quick Links</a><a href="#">Some Quick Links</a><a href="#">Some Quick Links</a><a href="#">Some Quick Links</a><a href="#">Some Quick Links</a></nav>
  <div class="col-rule abs" style="left:924px"></div>
  <div class="follow abs">Follow us</div>
  <span class="social abs" style="left:960px"></span>
  <span class="social abs" style="left:998px"></span>
  <div class="footer-search abs">Search<i></i></div>
  <p class="copyright abs">Copyright ©201 Velorast Biologics</p>
</footer>

</body>
</html>
```